Mortgage Broking boutique Business

I’m wanting a revamped look to my existing business card design. I do like the black and silver but happy to have other colours introduced based on your creation. I’ve attached a copy of my current card so you can have a starting point updated details noted brloe. I deal with high net worth individuals so need my card to be sophisticated, classy that gives off a classy vibe

Target Market(s)

High net worth, wealthy

Industry/Entity Type

Mortgage Brokerage

Contact Information for Business Card

Job title: Finance Executive
Phone: +61 7 3287 4419
Mobile: 0471 352 608
Email: marcus@quillbrookcapital.com.au
Web: www.quillbrookcapital.com.au
Address: level 36 Tindale Court, 58 Harwick St Brisbane QLD 4000

Font styles to use
Other font styles liked:
• Helvetica

Colors

Designer to choose colors to be used in the design.

Requirements
Must have
• Use my existing card design as a starting point

```html
<!DOCTYPE html>
<html lang="en">
<head>
<meta charset="utf-8">
<title>Quillbrook Capital — Business Card</title>
<link rel="stylesheet" href="https://fonts.googleapis.com/css2?family=Montserrat:wght@400;500&display=swap">
<style>
  :root {
    --backdrop: #1b1b1b;
    --card: #0b0b0b;
    --card-glow: #1c1c1c;
    --ink: #f2f2f2;
    --ink-muted: #a9a9a9;
    --rule: #6e6e6e;
    --silver-dark: #6f6f6f;
    --silver-mid: #bdbdbd;
    --silver-light: #ffffff;
  }
  * { box-sizing: border-box; margin: 0; padding: 0; }
  html, body {
    width: 1200px; height: 1200px; overflow: hidden;
    background: var(--backdrop);
    font-family: "Montserrat", Helvetica, Arial, sans-serif;
    color: var(--ink);
  }
  .sheet {
    position: relative; width: 1200px; height: 1200px;
    display: flex; flex-direction: column; align-items: center; justify-content: center; gap: 34px;
  }
  .card {
    position: relative; width: 900px; height: 514px;
    background: radial-gradient(ellipse at 55% 40%, var(--card-glow), var(--card) 70%);
  }
  /* silver frames */
  .frame {
    position: absolute; pointer-events: none;
    border: solid transparent;
    background:
      linear-gradient(var(--card), var(--card)) padding-box,
      linear-gradient(120deg, var(--silver-dark), var(--silver-light) 30%, var(--silver-dark) 55%, var(--silver-light) 80%, var(--silver-mid)) border-box;
  }
  .frame--inner-hollow { background:
      linear-gradient(transparent, transparent) padding-box,
      linear-gradient(120deg, var(--silver-dark), var(--silver-light) 30%, var(--silver-dark) 55%, var(--silver-light) 80%, var(--silver-mid)) border-box;
    -webkit-mask: linear-gradient(#000 0 0) border-box, linear-gradient(#000 0 0) padding-box;
    -webkit-mask-composite: xor; mask-composite: exclude;
  }

  /* front */
  .card--front .frame-outer { inset: 0; border-width: 14px; }
  .card--front .frame-line { inset: 30px; border-width: 3px; }
  .card--front .frame-outer, .card--front .frame-line { background: none;
    border-image: linear-gradient(120deg, var(--silver-dark), var(--silver-light) 30%, var(--silver-dark) 55%, var(--silver-light) 80%, var(--silver-mid)) 1; }
  .front-brand {
    position: absolute; left: 0; right: 0; top: 178px; text-align: center;
  }
  .wordmark { font-weight: 400; color: var(--ink); letter-spacing: 0.26em; text-transform: uppercase; line-height: 1.25; }
  .front-brand .wordmark { font-size: 44px; }
  .front-web {
    position: absolute; left: 0; right: 0; bottom: 64px; text-align: center;
    font-size: 19px; letter-spacing: 0.06em; font-weight: 500;
  }

  /* back */
  .card--back .frame-line { position: absolute; inset: 26px; border: 4px solid;
    border-image: linear-gradient(120deg, var(--silver-dark), var(--silver-light) 30%, var(--silver-dark) 55%, var(--silver-light) 80%, var(--silver-mid)) 1; }
  .back-brand { position: absolute; left: 62px; top: 62px; }
  .back-brand .wordmark { font-size: 38px; }
  .brand-dot {
    position: absolute; right: 70px; top: 150px; width: 80px; height: 80px; border-radius: 50%;
    background: linear-gradient(135deg, var(--silver-light), var(--silver-dark) 60%, var(--silver-mid));
  }
  .person { position: absolute; left: 62px; top: 218px; width: 776px; }
  .person-name { font-size: 31px; font-weight: 500; letter-spacing: 0.05em; text-transform: uppercase; }
  .person-title { font-size: 18px; color: var(--ink-muted); letter-spacing: 0.16em; text-transform: uppercase; margin-top: 2px; }
  .person-rule { height: 1px; background: var(--rule); margin-top: 10px; }
  .contact { list-style: none; margin-top: 10px; }
  .contact li { display: flex; align-items: center; gap: 12px; font-size: 18px; line-height: 30px; letter-spacing: 0.03em; }
  .contact svg { width: 18px; height: 18px; flex: none; fill: none; stroke: var(--ink-muted); stroke-width: 1.6; }
  .address {
    position: absolute; right: 70px; top: 392px; width: 360px; text-align: right;
    border-top: 1px solid var(--rule); padding-top: 8px;
    font-size: 18px; line-height: 28px; letter-spacing: 0.03em; font-style: normal;
  }
</style>
</head>
<body>
<main class="sheet">
  <section class="card card--front" aria-label="Card front">
    <div class="frame-outer" style="position:absolute"></div>
    <div class="frame-line" style="position:absolute"></div>
    <div class="front-brand">
      <p class="wordmark">Quillbrook<br>Capital</p>
    </div>
    <p class="front-web">WWW.QUILLBROOKCAPITAL.COM.AU</p>
  </section>

  <section class="card card--back" aria-label="Card back">
    <div class="frame-line"></div>
    <div class="back-brand"><p class="wordmark">Quillbrook Capital</p></div>
    <div class="brand-dot"></div>
    <div class="person">
      <p class="person-name">Marcus Ellery</p>
      <p class="person-title">Finance Executive</p>
      <div class="person-rule"></div>
      <ul class="contact">
        <li><svg viewBox="0 0 18 18"><rect x="5" y="1.5" width="8" height="15" rx="1.5"/><line x1="8" y1="14" x2="10" y2="14"/></svg>0471 352 608</li>
        <li><svg viewBox="0 0 18 18"><path d="M2 6c0-2 3-3 7-3s7 1 7 3v1h-3V5.5H5V7H2z"/><rect x="4" y="9" width="10" height="6" rx="1"/></svg>+61 7 3287 4419</li>
        <li><svg viewBox="0 0 18 18"><rect x="1.5" y="4" width="15" height="10"/><polyline points="1.5,4 9,10 16.5,4"/></svg>marcus@quillbrookcapital.com.au</li>
        <li><svg viewBox="0 0 18 18"><circle cx="9" cy="9" r="7"/><ellipse cx="9" cy="9" rx="3" ry="7"/><line x1="2" y1="9" x2="16" y2="9"/></svg>www.quillbrookcapital.com.au</li>
      </ul>
    </div>
    <address class="address">level 36 Tindale Court<br>58 Harwick St Brisbane QLD 4000</address>
  </section>
</main>
</body>
</html>
```